Landing page for web3 game airdrop

We need a specialist to create landing pages.

- Someone who understands the cycle of ideation > creation > measurement > adjustment > ideation > etc.
- Not one size fits all, but many segments/journeys.
- Experience with crypto and airdrops is a must.
- Experience with gaming and web3 is nice to have.

The landing page we need now is a page that explains our airdrop campaign and have people sign up.

Elements we want:
- Attention > Hero
- Interest > use case
- Desire > benefits
- Conviction > social proof/current success
- Action > CTA

Our website: https://velmora.com/
Current temporary landing page: https://7kqtz391.pagewisp.com/
Registration page: https://accounts.velmora.com/

For colors and fonts: keep to the colors of our website (velmora.com)
For background info: read our whitepaper.velmora.com

Target Market(s)

Web3 gamers, airdrop hunters, crypto interested

Font styles to use
Other font styles liked:
• keep the current ones on velmora.com

Colors

Designer to choose colors to be used in the design.

Requirements
Must have
• The flow as described: attention > interest > desire > conviction > action. If you have more ideas: of course welcome!
Nice to have
• Link with gaming, showing that we are special

```html
<!DOCTYPE html>
<html lang="en">
<head>
<meta charset="utf-8">
<title>Velmora — Web3 Game Airdrop</title>
<link href="https://fonts.googleapis.com/css2?family=Saira:wght@500;700;800&family=Poppins:wght@400;500;600&display=swap" rel="stylesheet">
<style>
:root{
  --bg-deep:#08060f;
  --bg-night:#0d0a1c;
  --purple:#3a2470;
  --purple-card:#2c1d55;
  --purple-ring:#5b3aa8;
  --violet:#6e45c8;
  --orange:#ffa200;
  --orange-dark:#f08a00;
  --white:#ffffff;
  --muted:#d9d4ea;
  --line:#2b2640;
}
*{margin:0;padding:0;box-sizing:border-box}
html,body{width:1200px;height:4019px;overflow:hidden;background:var(--bg-deep)}
body{position:relative;font-family:"Poppins",sans-serif;color:var(--white)}
.abs{position:absolute}
.heading{font-family:"Saira",sans-serif;font-weight:800;text-transform:uppercase;letter-spacing:.5px;line-height:1.12}
.brand{font-family:"Saira",sans-serif;font-weight:500;letter-spacing:6px;text-transform:uppercase;color:var(--white)}
.btn{position:absolute;display:flex;align-items:center;justify-content:center;background:var(--orange);color:var(--white);font-family:"Saira",sans-serif;font-weight:700;font-size:13px;text-transform:uppercase;border-radius:3px;letter-spacing:.3px}
.underline{position:absolute;height:3px;width:110px;left:545px;background:linear-gradient(90deg,transparent,var(--orange),transparent);border-radius:2px}
.center{text-align:center;left:0;width:1200px}

/* header */
.site-header{top:0;left:0;width:1200px;height:80px;background:#0b0a24}
.menu-btn{left:87px;top:24px;width:38px;height:32px;border:1.5px solid #fff;border-radius:5px;display:flex;flex-direction:column;justify-content:center;align-items:center;gap:3px}
.menu-btn span{width:12px;height:2px;background:#fff}
.header-logo{left:0;width:1200px;top:22px;text-align:center;font-size:30px}
.login{left:933px;top:30px;font-size:12px;font-weight:600}

/* hero */
.hero{top:80px;left:0;width:1200px;height:477px;background:
 radial-gradient(ellipse 200px 320px at 600px 40px,rgba(110,200,255,.55),transparent 70%),
 radial-gradient(ellipse 420px 300px at 820px 300px,rgba(150,70,60,.45),transparent 70%),
 radial-gradient(ellipse 500px 400px at 300px 200px,rgba(60,60,170,.6),transparent 70%),
 linear-gradient(180deg,#2a1f6a 0%,#1d1a55 45%,#231440 100%)}
.hero-art{left:470px;top:120px;width:700px;height:437px;background:radial-gradient(ellipse at 50% 60%,rgba(90,160,70,.35),rgba(200,170,60,.25) 40%,rgba(170,40,40,.25) 65%,transparent 80%)}
.hero-title{left:84px;top:208px;font-size:45px}
.scroll{left:1130px;top:200px;width:24px}
.scroll-text{left:1136px;top:225px;font-size:9px;writing-mode:vertical-rl;color:#ddd}
.dot{position:absolute;left:1138px;width:8px;height:8px;border-radius:50%;background:#fff}

/* how it works */
.how{top:557px;left:0;width:1200px;height:629px;background:
 radial-gradient(ellipse 500px 260px at 600px 330px,rgba(40,80,40,.45),transparent 75%),
 linear-gradient(180deg,#2a1850 0%,#1b1233 40%,#120c22 100%)}
.lead{font-size:12.5px;line-height:19px;color:var(--muted)}
.step-icon{position:absolute;width:138px;height:138px;border-radius:50%;background:var(--purple);border:8px solid var(--purple-ring);display:flex;align-items:center;justify-content:center}
.step-label{position:absolute;width:240px;text-align:center;font-family:"Saira",sans-serif;font-weight:800;font-size:15px;color:var(--orange)}
.step-text{position:absolute;width:210px;text-align:center;font-size:12px;line-height:19px;color:var(--muted)}

/* benefits */
.benefits{top:1186px;left:0;width:1200px;height:1000px;background:#060509}
.person-art{left:0;top:1428px;width:546px;height:741px;background:radial-gradient(ellipse 220px 360px at 280px 380px,#1f3448,#121a26 55%,transparent 80%)}
.benefit-card{position:absolute;left:584px;width:486px;background:var(--purple-card)}
.benefit-ring{position:absolute;left:514px;width:138px;height:138px;border-radius:50%;background:#241a48;border:8px solid var(--purple-ring);display:flex;align-items:center;justify-content:center}
.benefit-title{position:absolute;left:104px;top:32px;font-family:"Saira",sans-serif;font-weight:800;font-size:13px;text-transform:uppercase}
.benefit-text{position:absolute;left:104px;top:60px;width:340px;font-size:11.5px;line-height:19px;color:var(--muted)}

/* earn */
.earn{top:2114px;left:0;width:1200px;height:539px;background:linear-gradient(180deg,#241a4a,#181238 60%,#120d2c);clip-path:polygon(0 10%,40% 0,100% 17%,100% 100%,0 100%)}
.bull-art{left:452px;top:2231px;width:718px;height:375px;background:radial-gradient(ellipse 260px 180px at 260px 180px,rgba(240,190,60,.75),rgba(180,120,20,.35) 55%,transparent 80%)}
.earn-title{left:97px;top:2308px;font-size:44px}

/* walkthrough */
.walk{top:2653px;left:0;width:1200px;height:935px;background:radial-gradient(ellipse 600px 380px at 600px 300px,#141a1a,#07070b 80%)}
.video-frame{left:130px;top:2897px;width:940px;height:498px;background:var(--purple);border-radius:4px}
.video-still{left:148px;top:2922px;width:905px;height:456px;background:radial-gradient(ellipse 300px 200px at 50% 70%,#4b5a2a,transparent 70%),linear-gradient(180deg,#2b2f2a,#243318 55%,#2e3b1e)}
.play{left:937px;top:3276px;width:76px;height:76px;border-radius:50%;background:#5a3aa0;border:5px solid #7b55d0;display:flex;align-items:center;justify-content:center}
.partner{position:absolute;top:3474px;height:32px;background:#e8e6f0;border-radius:4px;opacity:.9}

/* footer */
.site-footer{top:3588px;left:0;width:1200px;height:431px;background:#05050a}
.footer-logo{left:0;width:1200px;top:3628px;text-align:center;font-size:40px}
.rule{left:130px;width:940px;height:1px;background:var(--line)}
.nl-title{left:130px;top:3757px;font-family:"Saira",sans-serif;font-weight:800;font-size:17px;text-transform:uppercase}
.nl-input{left:130px;top:3808px;font-size:12px}
.nl-line{left:130px;top:3846px;width:300px;height:1px;background:#888}
.contact-icon{position:absolute;left:563px;width:30px;height:30px;border-radius:50%;background:var(--violet);display:flex;align-items:center;justify-content:center}
.contact{position:absolute;left:609px;font-size:11px;line-height:17px}
.vrule{position:absolute;top:3770px;width:1px;height:85px;background:var(--line)}
.links{position:absolute;font-size:11px;line-height:19px}
.copyright{top:3953px;font-size:11px;color:#eee}
</style>
</head>
<body>

<header class="abs site-header">
  <div class="abs menu-btn"><span></span><span></span><span></span></div>
  <div class="abs brand header-logo">Velmora</div>
  <div class="abs login">LOGIN</div>
  <div class="btn" style="left:997px;top:23px;width:116px;height:34px">Join Now</div>
</header>

<section class="abs hero">
</section>
<div class="abs hero-art" role="img" aria-label="Three armoured game heroes standing in a glowing jungle cave"></div>
<h1 class="abs heading hero-title">Velmora<br>Web3 Game<br>Velmora</h1>
<div class="btn" style="left:86px;top:378px;width:146px;height:37px">Join Now</div>
<div class="abs scroll-text">Scroll Down →</div>
<div class="dot" style="top:333px"></div>
<div class="dot" style="top:350px"></div>
<div class="dot" style="top:367px"></div>
<div class="dot" style="top:383px;left:1135px;width:14px;height:14px;background:none;border:2px solid #fff"></div>
<div class="dot" style="top:407px"></div>

<section class="abs how"></section>
<h2 class="abs heading center" style="top:618px;font-size:37px">How It Works</h2>
<div class="underline" style="top:678px"></div>
<p class="abs lead center" style="top:700px">Velmora's airdrop campaign is massive! We drop 25 million $VLM<br>worth $87,500 And you can easily join!</p>

<div class="step-icon" style="left:167px;top:794px">
  <svg width="64" height="64" viewBox="0 0 64 64" fill="none" stroke="#fff" stroke-width="2.5"><rect x="8" y="10" width="48" height="32" rx="4"/><circle cx="22" cy="23" r="5"/><path d="M14 35c2-5 14-5 16 0M36 20h14M36 27h14M36 34h8"/><path d="M28 58l-6-10 4-2 4 6V40l4 0v10l8 2v6"/></svg>
</div>
<div class="step-icon" style="left:530px;top:794px">
  <svg width="64" height="64" viewBox="0 0 64 64" fill="none" stroke="#fff" stroke-width="2.5"><rect x="10" y="26" width="44" height="30" rx="4"/><rect x="40" y="35" width="14" height="10" rx="2"/><circle cx="32" cy="18" r="11"/><path d="M35 13h-4a3 3 0 0 0 0 6h2a3 3 0 0 1 0 6h-4M32 10v2M32 25v2"/></svg>
</div>
<div class="step-icon" style="left:894px;top:794px">
  <svg width="64" height="64" viewBox="0 0 64 64" fill="none" stroke="#fff" stroke-width="2.5"><circle cx="26" cy="20" r="9"/><path d="M8 50c0-12 8-18 18-18 6 0 10 2 13 5"/><circle cx="46" cy="44" r="11"/><path d="M49 39h-4a2.5 2.5 0 0 0 0 5h2a2.5 2.5 0 0 1 0 5h-4M46 36v2M46 49v2"/><path d="M40 8a24 24 0 0 1 16 16" stroke-dasharray="3 4"/></svg>
</div>
<svg class="abs" style="left:342px;top:840px" width="150" height="40" viewBox="0 0 150 40" fill="none" stroke="#ffa200" stroke-width="2"><path d="M2 22C40 2 100 4 140 24" stroke-dasharray="6 5"/><path d="M134 16l8 8-10 4"/></svg>
<svg class="abs" style="left:697px;top:840px" width="150" height="40" viewBox="0 0 150 40" fill="none" stroke="#ffa200" stroke-width="2"><path d="M2 22C40 2 100 4 140 24" stroke-dasharray="6 5"/><path d="M134 16l8 8-10 4"/></svg>

<div class="step-label" style="left:116px;top:953px">Step 1</div>
<div class="step-label" style="left:479px;top:953px">Step 2</div>
<div class="step-label" style="left:843px;top:953px">Step 3</div>
<p class="step-text" style="left:131px;top:985px">Sign up and confirm your email address. Then secure your account with a password.</p>
<p class="step-text" style="left:484px;top:985px;width:230px">Connect your socials (Chirp, Wirecast or Guildhall) and your wallet.</p>
<p class="step-text" style="left:858px;top:985px">Start doing missions and invite your friends. The more Power you earn, the larger your share of the 25 million $VLM.</p>
<div class="btn" style="left:510px;top:1089px;width:175px;height:38px">Velmora Sign Up</div>

<section class="abs benefits"></section>
<h2 class="abs heading center" style="top:1243px;font-size:28px">Velmora Benefits</h2>
<div class="underline" style="top:1298px"></div>
<p class="abs lead" style="left:250px;width:700px;top:1326px;text-align:center;font-size:12.5px;line-height:22px">Sed ut perspiciatis unde omnis iste natus error sit voluptatem accusantium doloremque laudantium, totam rem aperiam, eaque ipsa quae ab illo inventore veritatis et quasi architecto beatae vitae dicta sunt explicabo. Nemo enim ipsam voluptatem quia voluptas sit aspernatur</p>
<div class="abs person-art" role="img" aria-label="Young gamer in a glowing VR headset and jacket"></div>

<div class="benefit-card" style="top:1470px;height:168px">
  <div class="benefit-title">Nemo enim ipsam voluptatem</div>
  <p class="benefit-text">Sed ut perspiciatis unde omnis iste natus error sit voluptatem accusantium doloremque laudantium, totam rem aperiam, eaque ipsa quae ab illo inventore veritatis et quasi architecto beatae vitae dicta sunt explicabo.</p>
</div>
<div class="benefit-card" style="top:1666px;height:170px">
  <div class="benefit-title">Nemo enim ipsam voluptatem</div>
  <p class="benefit-text">Sed ut perspiciatis unde omnis iste natus error sit voluptatem accusantium doloremque laudantium, totam rem aperiam, eaque ipsa quae ab illo inventore veritatis et quasi architecto beatae vitae dicta sunt explicabo.</p>
</div>
<div class="benefit-card" style="top:1865px;height:168px">
  <div class="benefit-title">Nemo enim ipsam voluptatem</div>
  <p class="benefit-text">Sed ut perspiciatis unde omnis iste natus error sit voluptatem accusantium doloremque laudantium, totam rem aperiam, eaque ipsa quae ab illo inventore veritatis et quasi architecto beatae vitae dicta sunt explicabo.</p>
</div>
<div class="benefit-ring" style="top:1485px">
  <svg width="62" height="62" viewBox="0 0 64 64" fill="none" stroke="#fff" stroke-width="2.2"><rect x="14" y="8" width="26" height="42" rx="4" transform="rotate(-15 27 29)"/><circle cx="36" cy="36" r="9"/><path d="M36 31v10M32 36h8M10 54h40M14 58h32"/></svg>
</div>
<div class="benefit-ring" style="top:1682px">
  <svg width="62" height="62" viewBox="0 0 64 64" fill="none" stroke="#fff" stroke-width="2.2"><circle cx="32" cy="32" r="11"/><path d="M35 27h-4a2.5 2.5 0 0 0 0 5h2a2.5 2.5 0 0 1 0 5h-4M32 24v2M32 37v2"/><path d="M32 21V8M32 43v13M21 32H8M43 32h13M24 24l-8-8M40 24l8-8M24 40l-8 8M40 40l8 8"/><circle cx="32" cy="6" r="2.5"/><circle cx="32" cy="58" r="2.5"/><circle cx="6" cy="32" r="2.5"/><circle cx="58" cy="32" r="2.5"/></svg>
</div>
<div class="benefit-ring" style="top:1879px">
  <svg width="62" height="62" viewBox="0 0 64 64" fill="none" stroke="#fff" stroke-width="2.2"><rect x="26" y="10" width="24" height="40" rx="4" transform="rotate(15 38 30)"/><circle cx="22" cy="26" r="11"/><path d="M25 21h-4a2.5 2.5 0 0 0 0 5h2a2.5 2.5 0 0 1 0 5h-4M22 18v2M22 31v2M30 40h12M30 46h10"/></svg>
</div>

<section class="abs earn"></section>
<div class="abs bull-art" role="img" aria-label="Golden low-poly bull beside a large gold coin on stacked gold bars"></div>
<h2 class="abs heading earn-title">Earn Power and<br>Secure Your Share<br>Today</h2>
<div class="btn" style="left:98px;top:2476px;width:147px;height:38px">Join Now</div>

<section class="abs walk"></section>
<h2 class="abs heading center" style="top:2733px;font-size:37px">Watch the Walkthrough</h2>
<div class="underline" style="top:2790px"></div>
<p class="abs lead center" style="top:2814px">Velmora's airdrop campaign is massive! We drop 25 million $VLM<br>worth $87,500 And you can easily join!</p>
<div class="abs video-frame"></div>
<div class="abs video-still" role="img" aria-label="Gameplay still of an explorer on a jungle path with a registration form on screen"></div>
<div class="abs play"><svg width="26" height="26" viewBox="0 0 24 24"><path d="M7 4l13 8-13 8z" fill="#fff"/></svg></div>

<div class="partner" style="left:130px;width:108px"></div>
<div class="partner" style="left:296px;width:74px"></div>
<div class="partner" style="left:433px;width:66px"></div>
<div class="partner" style="left:562px;width:172px"></div>
<div class="partner" style="left:786px;width:120px"></div>
<div class="partner" style="left:958px;width:112px"></div>

<footer class="abs site-footer"></footer>
<div class="abs brand footer-logo">Velmora</div>
<div class="abs rule" style="top:3713px"></div>
<div class="abs nl-title">Sign Up for Newsletter</div>
<div class="abs nl-input">Enter your email</div>
<div class="abs nl-line"></div>
<div class="btn" style="left:409px;top:3812px;width:98px;height:36px;border-radius:0">Subscribe</div>

<div class="contact-icon" style="top:3762px"><svg width="16" height="16" viewBox="0 0 24 24" fill="none" stroke="#fff" stroke-width="2"><path d="M5 3h4l2 5-3 2a11 11 0 0 0 6 6l2-3 5 2v4a2 2 0 0 1-2 2A17 17 0 0 1 3 5a2 2 0 0 1 2-2z"/></svg></div>
<div class="contact" style="top:3761px">Telephone:<br>+1 555 01200 48000</div>
<div class="contact-icon" style="top:3817px"><svg width="16" height="16" viewBox="0 0 24 24" fill="none" stroke="#fff" stroke-width="2"><path d="M3 11l18-7-6 17-3-7z"/></svg></div>
<div class="contact" style="top:3816px">Email Us<br>info@velmora.com</div>
<div class="vrule" style="left:770px"></div>
<div class="links" style="left:815px;top:3756px">Contact Us<br>Terms &amp; Conditions<br>Privacy Policy<br>Disclaimer</div>
<div class="vrule" style="left:955px"></div>
<div class="links" style="left:997px;top:3756px">Whitepaper<br>Support<br>Blog<br>Wiki<br>Community</div>
<div class="abs rule" style="top:3900px"></div>
<p class="abs copyright center">Velmora © 2024. All Rights Reserved. Imprint | Cookie Policy | Sitemap</p>

</body>
</html>
```